Customer Dashboard Design for Email Security SaaS

Mailvarden is a commercial email spam filter offered as a SaaS product, built and operated by a small German hosting provider. It protects business email accounts against spam, phishing, scam, and viruses using a multilayer filtering pipeline that combines traditional spam detection with AI-powered classification. The product runs entirely on German infrastructure, ensuring data sovereignty for European customers.

We need a complete redesign of the customer-facing dashboard. This is the web application where paying customers manage their email filtering: view their mail log, check quarantined emails, manage allow/blocklists, configure their settings, and handle their subscription. It is the primary touchpoint between Mailvarden and its customers.

Our customers are system administrators, IT managers at small-to-medium businesses, and operators of small hosting providers. They are technically competent but not designers. They expect professional, efficient tools that respect their time. They typically manage 10–500 email accounts and check the dashboard a few times per week, with heavier use during spam incidents.

We have attached the current mockups which really need to be replaced with something good looking.

Target Market(s)

System administrators, IT managers at small-to-medium businesses, and operators of small hosting providers.

Industry/Entity Type

SaaS

Number of Pages Required

5+ page

```html
<!DOCTYPE html>
<html lang="en">
<head>
<meta charset="utf-8">
<title>Mailvarden – Quarantäne</title>
<link href="https://fonts.googleapis.com/css2?family=Poppins:wght@400;500;600;700&display=swap" rel="stylesheet">
<style>
:root{
  --bg:#1c1b1b;
  --panel:#242222;
  --panel-edge:#302e2e;
  --card:#222020;
  --text:#ffffff;
  --muted:#c9c6c4;
  --line:#4a4746;
  --green:#0a9a6c;
  --green-dark:#0f3a2c;
  --red:#c95a5a;
  --badge-red:#d9534f;
  --badge-amber:#d9a24a;
  --admin:#3a3838;
}
*{box-sizing:border-box;margin:0;padding:0}
html,body{width:1200px;height:750px;overflow:hidden}
body{background:var(--bg);font-family:'Poppins',sans-serif;color:var(--text);position:relative}
.sidebar{position:absolute;left:17px;top:15px;width:199px;height:720px;border-radius:22px;background:linear-gradient(180deg,#272424,#1f1d1d);border:1px solid var(--panel-edge)}
.brand{position:absolute;top:27px;left:0;width:100%;text-align:center}
.brand-mark{width:45px;height:45px;border-radius:10px;background:var(--green);margin:0 auto}
.brand-name{font-size:23px;font-weight:500;margin-top:6px;letter-spacing:-.2px}
.nav{position:absolute;top:150px;left:18px;width:162px;list-style:none}
.nav li{display:flex;align-items:center;height:33px;padding-left:15px;font-size:10.5px;color:var(--text)}
.nav li svg{width:15px;height:15px;margin-right:11px;stroke:#9c9896;fill:none;stroke-width:1.4}
.nav li.active{background:var(--green);border-radius:10px;height:41px;margin:4px 0 8px}
.nav li.active svg{stroke:#fff}
.nav li.active .chev{margin-left:auto;margin-right:12px;width:9px;height:9px;stroke-width:2}
.nav li.gap{margin-top:0}
.sidebar-foot{position:absolute;left:18px;top:606px;width:162px;border-top:1px solid var(--panel-edge);text-align:center}
.foot-label{font-size:9px;font-weight:600;margin-top:15px;letter-spacing:.2px}
.admin-btn{margin-top:14px;height:41px;border-radius:10px;background:var(--admin);display:flex;align-items:center;justify-content:center;font-size:9.5px;font-weight:600;gap:6px}
.admin-btn svg{width:11px;height:11px;fill:#fff}
.page-icon{position:absolute;left:260px;top:42px;width:46px;height:46px;border-radius:10px;border:1px solid var(--panel-edge);background:#222020;display:flex;align-items:center;justify-content:center}
.page-icon svg{width:18px;height:18px;stroke:#fff;fill:none;stroke-width:1.5}
.page-title{position:absolute;left:320px;top:33px;font-size:24px;font-weight:600}
.page-sub{position:absolute;left:321px;top:70px;font-size:11px;color:var(--muted)}
.theme-toggle{position:absolute;left:1105px;top:41px;width:50px;height:27px;border-radius:14px;background:#fff;display:flex;align-items:center;padding:0 3px;justify-content:space-between}
.theme-toggle .knob{width:21px;height:21px;border-radius:50%;background:#1c1b1b;display:flex;align-items:center;justify-content:center}
.theme-toggle svg{width:12px;height:12px;fill:none;stroke-width:1.6}
.notice{position:absolute;left:261px;top:121px;width:894px;height:77px;border-radius:24px;border:1px solid #22352d;background:linear-gradient(90deg,#1e1d1d 0%,#173328 55%,#13402f 100%);display:flex;align-items:center;padding-left:31px;font-size:14.5px;font-weight:700}
.checkbox{width:13.5px;height:13.5px;border:1.3px solid #9c9896;border-radius:2px;position:absolute}
.select-all{position:absolute;left:283px;top:233px;font-size:11px;color:var(--muted)}
.btn{border:none;border-radius:9px;color:#fff;font-family:'Poppins',sans-serif;font-weight:600;font-size:8.5px;letter-spacing:.1px;display:flex;align-items:center;justify-content:center}
.btn-release{background:var(--green)}
.btn-delete{background:var(--red)}
.btn-details{background:#fff;color:#111}
.bulk{position:absolute;top:221px;height:41px;width:161px;border-radius:11px;font-size:9px}
.mail-card{position:absolute;left:286px;width:407px;height:164px;border-radius:24px;border:1px solid var(--panel-edge);background:linear-gradient(180deg,#252222,#1f1d1d);padding:25px 22px 0 29px}
.mail-head{display:flex;justify-content:space-between}
.sender{font-size:9.5px;color:var(--muted)}
.subject{font-size:11.5px;font-weight:500;margin-top:3px}
.badge{height:18px;padding:0 12px;border:1px solid;border-radius:2px;font-size:9px;display:flex;align-items:center;margin-top:1px}
.badge.phishing{color:var(--badge-red);border-color:var(--badge-red)}
.badge.newsletter{color:var(--badge-amber);border-color:var(--badge-amber)}
.mail-meta{border-top:1px solid var(--line);margin-top:17px;padding-top:10px;display:flex;justify-content:space-between;font-size:9.5px;color:var(--muted);padding-right:3px}
.mail-actions{display:flex;gap:6px;margin-top:13px}
.mail-actions .btn{width:114px;height:32px;border-radius:7px}
</style>
</head>
<body>
<aside class="sidebar">
  <div class="brand">
    <div class="brand-mark"></div>
    <div class="brand-name">Mailvarden</div>
  </div>
  <ul class="nav">
    <li><svg viewBox="0 0 16 16"><path d="M2 8 8 2.5 14 8M3.5 6.8V14h9V6.8M6.5 14v-4h3v4"/></svg>Dashboard</li>
    <li><svg viewBox="0 0 16 16"><path d="M5 3.5h9M5 6.5h9M5 9.5h9M5 12.5h9M2 3.5h1M2 6.5h1M2 9.5h1M2 12.5h1"/></svg>Mail Log</li>
    <li><svg viewBox="0 0 16 16"><rect x="1.5" y="3.5" width="13" height="9" rx="1.5"/><path d="m2 4.5 6 4.5 6-4.5"/></svg>Mailboxes</li>
    <li><svg viewBox="0 0 16 16"><path d="M8 1.5 13.5 3.5v4c0 3.5-2.5 6-5.5 7-3-1-5.5-3.5-5.5-7v-4z"/><path d="m5.5 8 1.8 1.8L10.8 6.3"/></svg>Allowlist</li>
    <li><svg viewBox="0 0 16 16"><path d="M8 1.5 13.5 3.5v4c0 3.5-2.5 6-5.5 7-3-1-5.5-3.5-5.5-7v-4z"/><path d="M8 5v3.5M8 10.5v.5"/></svg>Blocklist</li>
    <li class="active"><svg viewBox="0 0 16 16"><rect x="3" y="7" width="10" height="7.5" rx="1.5"/><path d="M5.5 7V4.8a2.5 2.5 0 0 1 5-.3M8 10v1.8"/></svg>Quarantine<svg class="chev" viewBox="0 0 10 10"><path d="m3 1 4 4-4 4"/></svg></li>
    <li><svg viewBox="0 0 16 16"><circle cx="8" cy="8" r="2.3"/><path d="M8 1.5v2M8 12.5v2M1.5 8h2M12.5 8h2M3.4 3.4l1.4 1.4M11.2 11.2l1.4 1.4M3.4 12.6l1.4-1.4M11.2 4.8l1.4-1.4"/></svg>Settings</li>
    <li><svg viewBox="0 0 16 16"><rect x="2" y="7" width="8" height="7.5" rx="1"/><rect x="9" y="9" width="5" height="5.5" rx=".8"/><path d="M4.5 7V4.5h3V7M5 2.5h2"/></svg>Billing</li>
  </ul>
  <div class="sidebar-foot">
    <div class="foot-label">VERWALTUNG</div>
    <div class="admin-btn"><svg viewBox="0 0 12 12"><circle cx="6" cy="3.2" r="2.6"/><path d="M1 12c0-3 2.2-5 5-5s5 2 5 5z"/></svg>ADMINISTRATION</div>
  </div>
</aside>

<div class="page-icon"><svg viewBox="0 0 18 18"><rect x="3.5" y="8" width="11" height="8.5" rx="2"/><path d="M6 8V5.2a3 3 0 0 1 6-.5M9 11.2v2"/></svg></div>
<h1 class="page-title">Quarantäne</h1>
<p class="page-sub">Review emails held back by the system</p>
<div class="theme-toggle">
  <span class="knob"><svg viewBox="0 0 12 12" stroke="#fff"><path d="M9.5 7.5A4 4 0 1 1 5 2.5a3.2 3.2 0 0 0 4.5 5z"/></svg></span>
  <svg viewBox="0 0 12 12" stroke="#222"><circle cx="6" cy="6" r="2.2"/><path d="M6 .8v1.3M6 9.9v1.3M.8 6h1.3M9.9 6h1.3M2.3 2.3l.9.9M8.8 8.8l.9.9M2.3 9.7l.9-.9M8.8 3.2l.9-.9"/></svg>
</div>

<div class="notice">Emails are automatically deleted after 14 days.</div>

<span class="checkbox" style="left:261px;top:235px"></span>
<span class="select-all">Select all</span>
<button class="btn btn-release bulk" style="left:825px">RELEASE SELECTED</button>
<button class="btn btn-delete bulk" style="left:995px">DELETE SELECTED</button>

<span class="checkbox" style="left:261px;top:300px"></span>
<article class="mail-card" style="top:300px">
  <div class="mail-head">
    <div><div class="sender">security@paybridge-alert.com</div><div class="subject">Unusual login attempt detected</div></div>
    <span class="badge phishing">Phishing</span>
  </div>
  <div class="mail-meta"><span>Apr 14, 2026</span><span>97%</span></div>
  <div class="mail-actions">
    <button class="btn btn-release">RELEASE SELECTED</button>
    <button class="btn btn-delete">DELETE SELECTED</button>
    <button class="btn btn-details">DETAILS</button>
  </div>
</article>

<span class="checkbox" style="left:261px;top:482px"></span>
<article class="mail-card" style="top:482px">
  <div class="mail-head">
    <div><div class="sender">offers@cartharbor.com</div><div class="subject">Weekend Deals - Limited Time</div></div>
    <span class="badge newsletter">Newsletter</span>
  </div>
  <div class="mail-meta"><span>Apr 14, 2026</span><span>97%</span></div>
  <div class="mail-actions">
    <button class="btn btn-release">RELEASE SELECTED</button>
    <button class="btn btn-delete">DELETE SELECTED</button>
    <button class="btn btn-details">DETAILS</button>
  </div>
</article>
</body>
</html>
```